Chiropractic healthcare group business card

We are a Portland Oregon based chiropractic healthcare group. Looking for a new business card design. Something cutting edge, that shows off our new logo and tag line.Use either of the attached logos.Our tag line = "Who could you be free of aches?"I'm open to about anything, impress me!!
Target Market(s)
Chiropractic patients - Auto injury, back pain, sports injuries, neck , shoulder, hip, knee, ankle pain.
Industry/Entity Type
Chiropractic
Contact Information for Business Card
Dr. Bram Holtvick, D.C.
Clinic name - Fernway Chiropractic
2 clinics
location #1
20418 NW Marwick Road
Unit 4
Cedar Hollow, ST 00133
Location #2
13529 SE Calloway Street
Brackenford ST 00236
Main phone line 555.555.0143
website : www.FernwayClinics.example
Tag line "Who could you be free of aches?"
Colors
Designer to choose colors to be used in the design.
Requirements
Must have
- Use the logo colors -- Want the orange color to be a TRUE orange.
- Both clinic address
- phone number
- website
- personal email - b.holtvick@ReliefBeginsHere.example
- tag line - "Who could you be free of aches?"

```html
<!DOCTYPE html>
<html lang="en">
<head>
<meta charset="utf-8">
<title>Fernway Chiropractic — Business Card</title>
<link rel="stylesheet" href="https://fonts.googleapis.com/css2?family=Open+Sans:wght@400;600;700&display=swap">
<style>
  :root {
    --orange: #f28a1a;
    --grey: #6b6b6b;
    --ink: #1e1e1e;
    --paper: #fbfaf8;
    --stripe: #f1eeea;
    --black: #121212;
    --black-soft: #262626;
    --brand-grey: #8a8a8a;
    --backdrop: #e7e4df;
  }
  * { box-sizing: border-box; margin: 0; padding: 0; }
  html, body { width: 1200px; height: 942px; overflow: hidden; }
  body {
    background: var(--backdrop);
    font-family: "Open Sans", Arial, sans-serif;
    color: var(--ink);
    position: relative;
  }
  .card {
    position: absolute;
    top: 121px;
    width: 400px;
    height: 700px;
    overflow: hidden;
    box-shadow: 0 6px 18px rgba(0,0,0,0.18);
  }
  .card-front {
    left: 160px;
    background: repeating-linear-gradient(-60deg, var(--paper) 0 6px, var(--stripe) 6px 8px);
  }
  .side-bands { position: absolute; left: 0; top: 0; }
  .brand {
    position: absolute;
    left: 70px;
    right: 20px;
    top: 150px;
    text-align: center;
    font-weight: 700;
    color: var(--ink);
  }
  .brand-name { font-size: 38px; letter-spacing: 10px; line-height: 1.1; }
  .brand-sub { font-size: 15px; letter-spacing: 4px; line-height: 1.4; }
  .contact-list {
    position: absolute;
    left: 84px;
    right: 22px;
    top: 300px;
    list-style: none;
  }
  .contact-row {
    display: flex;
    align-items: center;
    gap: 12px;
    min-height: 58px;
    padding: 8px 0;
    border-bottom: 2px solid var(--orange);
    font-size: 14px;
    line-height: 1.25;
  }
  .contact-row:last-child { border-bottom: none; }
  .contact-row.name { font-size: 16px; text-transform: uppercase; }
  .contact-row.email span { font-size: 13px; white-space: nowrap; }
  .contact-row.address { align-items: flex-end; }
  .address-text { display: flex; flex-direction: column; gap: 12px; }
  .address-line { display: block; }
  .icon { flex: none; width: 30px; height: 30px; }
  .card-back {
    left: 640px;
    background: linear-gradient(150deg, var(--black-soft) 0%, var(--black) 60%, #0b0b0b 100%);
  }
  .card-back .brand { left: 20px; top: 250px; color: var(--brand-grey); }
  .tagline {
    position: absolute;
    left: 30px;
    right: 30px;
    top: 560px;
    padding: 16px 0;
    border-top: 2px solid var(--orange);
    border-bottom: 2px solid var(--orange);
    color: #f2f2f2;
    font-size: 21px;
    text-align: center;
  }
</style>
</head>
<body>

<section class="card card-front" aria-label="Business card front">
  <svg class="side-bands" width="400" height="700" viewBox="0 0 400 700" aria-hidden="true">
    <polygon points="0,200 40,200 40,450 0,480" fill="var(--grey)"/>
    <polygon points="0,700 0,520 70,470 70,700" fill="var(--orange)"/>
  </svg>

  <div class="brand">
    <div class="brand-name">FERNWAY</div>
    <div class="brand-sub">CHIROPRACTIC</div>
  </div>

  <ul class="contact-list">
    <li class="contact-row name">
      <svg class="icon" viewBox="0 0 32 32" aria-hidden="true">
        <circle cx="16" cy="16" r="14" fill="none" stroke="var(--ink)" stroke-width="2.5"/>
        <circle cx="16" cy="12" r="5" fill="var(--ink)"/>
        <path d="M7 25c2-5 5-7 9-7s7 2 9 7z" fill="var(--ink)"/>
      </svg>
      <span>Dr. Bram Holtvick,<br>D.C.</span>
    </li>
    <li class="contact-row">
      <svg class="icon" viewBox="0 0 32 32" aria-hidden="true">
        <circle cx="16" cy="16" r="14" fill="none" stroke="var(--ink)" stroke-width="2.5"/>
        <path d="M11 9c-2 1-3 3-1 7s5 7 8 7 4-2 4-3l-3-3-2 2c-2-1-4-3-5-5l2-2-3-3z" fill="var(--ink)"/>
      </svg>
      <span>555.555.0143</span>
    </li>
    <li class="contact-row">
      <svg class="icon" viewBox="0 0 32 32" aria-hidden="true">
        <g fill="none" stroke="var(--ink)" stroke-width="2.2">
          <circle cx="16" cy="16" r="13"/>
          <ellipse cx="16" cy="16" rx="6" ry="13"/>
          <line x1="3" y1="16" x2="29" y2="16"/>
          <line x1="5" y1="10" x2="27" y2="10"/>
          <line x1="5" y1="22" x2="27" y2="22"/>
        </g>
      </svg>
      <span>www.FernwayClinics.example</span>
    </li>
    <li class="contact-row email">
      <svg class="icon" viewBox="0 0 32 32" aria-hidden="true">
        <rect x="3" y="7" width="26" height="19" fill="none" stroke="var(--ink)" stroke-width="2.5"/>
        <path d="M4 8l12 10 12-10" fill="none" stroke="var(--ink)" stroke-width="2.5"/>
      </svg>
      <span>b.holtvick@ReliefBeginsHere.example</span>
    </li>
    <li class="contact-row address">
      <svg class="icon" viewBox="0 0 32 32" aria-hidden="true">
        <path d="M3 15L16 5l13 10" fill="none" stroke="var(--ink)" stroke-width="2.5"/>
        <path d="M7 13v14h18V13" fill="none" stroke="var(--ink)" stroke-width="2.5"/>
        <path d="M16 13a4 4 0 0 1 4 4c0 3-4 7-4 7s-4-4-4-7a4 4 0 0 1 4-4z" fill="var(--ink)"/>
      </svg>
      <div class="address-text">
        <span class="address-block">
          <span class="address-line">20418 NW Marwick Road Unit 4</span>
          <span class="address-line">Cedar Hollow, ST 00133</span>
        </span>
        <span class="address-block">
          <span class="address-line">13529 SE Calloway Street Brackenford</span>
          <span class="address-line">ST 00236</span>
        </span>
      </div>
    </li>
  </ul>
</section>

<section class="card card-back" aria-label="Business card back">
  <div class="brand">
    <div class="brand-name">FERNWAY</div>
    <div class="brand-sub">CHIROPRACTIC</div>
  </div>
  <p class="tagline">Who could you be free of aches?</p>
</section>

</body>
</html>
```